Tidewell Electrical Solutions

On one side. LOGO (underneath:) Commercial Industrial Residential

- NAME & CONTACT DETAILS

Martin K. Oduya
Project Manager

(Cell icon) (441) 555-0187
(Email icon) twlelectricalsoultions@mailpost-demo.com
(Facebook & Instagram icons )@twlelectricalsolutions

Other side: LOGO - underneath ELECTRICAL CONSTRUCTION & MAINTENANCE . LED LIGHTING & AUTOMATION . LIFE SAFETY SYSTEMS (FIRE ALARM / SECURITY) . DATA & COMMUNICATION

```html
<!DOCTYPE html>
<html lang="en">
<head>
<meta charset="utf-8">
<title>Tidewell Electrical Solutions – Business Card</title>
<link href="https://fonts.googleapis.com/css2?family=Montserrat:wght@700&family=Questrial&display=swap" rel="stylesheet">
<style>
  :root{
    --teal:#0f5469;
    --ink:#2b2b2b;
    --white:#ffffff;
    --backdrop:#ececec;
  }
  *{margin:0;padding:0;box-sizing:border-box}
  html,body{width:1200px;height:1200px;overflow:hidden;background:var(--backdrop)}
  .stage{position:relative;width:1200px;height:1200px}
  .card{position:absolute;top:155px;width:375px;height:656px;overflow:hidden}
  .card-front{left:212px;background:var(--white);box-shadow:0 1px 3px rgba(0,0,0,.08)}
  .card-back{left:614px;background:var(--teal)}

  .wordmark{position:absolute;left:0;width:100%;display:flex;align-items:center;justify-content:center;gap:10px;
    font-family:"Questrial",sans-serif;font-size:21px;line-height:1;white-space:nowrap}
  .wordmark-dot{width:14px;height:14px;border-radius:50%;flex:none}
  .front-logo{top:106px;color:var(--teal)}
  .front-logo .wordmark-dot{background:var(--teal)}
  .back-logo{top:255px;color:var(--white)}
  .back-logo .wordmark-dot{background:var(--white)}

  .name-band{position:absolute;left:0;top:239px;width:336px;height:98px;
    background:var(--teal);border-radius:0 49px 49px 0;color:var(--white);padding:18px 0 0 26px}
  .person-name{font-family:"Montserrat",sans-serif;font-weight:700;font-size:26px;letter-spacing:.3px;text-transform:uppercase}
  .person-role{font-family:"Questrial",sans-serif;font-size:22px;margin-top:2px}

  .contact-list{position:absolute;left:0;top:0;width:100%;height:100%;list-style:none}
  .contact-rail{position:absolute;left:38px;top:371px;width:2px;height:175px;background:var(--teal)}
  .contact-item{position:absolute;left:22px;display:flex;align-items:center;gap:14px;
    font-family:"Questrial",sans-serif;font-size:17px;color:var(--ink);white-space:nowrap}
  .contact-icon{width:34px;height:34px;border-radius:50%;background:var(--teal);flex:none;
    display:flex;align-items:center;justify-content:center}
  .contact-email{font-size:14.5px}

  .circuit-band{position:absolute;left:0;top:0;width:100%;height:150px;
    background:linear-gradient(180deg,#2f6c80 0%,var(--teal) 100%)}

  .service-list{list-style:none}
  .service{position:absolute;left:0;display:flex;align-items:flex-start;
    font-family:"Questrial",sans-serif;font-size:17px;color:var(--white);line-height:25px;text-transform:uppercase}
  .service-plug{width:76px;height:25px;flex:none}
</style>
</head>
<body>
<main class="stage">

  <section class="card card-front" aria-label="Card front">
    <div class="wordmark front-logo">
      <span class="wordmark-dot"></span>
      <span>Tidewell Electrical Solutions</span>
    </div>

    <div class="name-band">
      <h1 class="person-name">Martin K. Oduya</h1>
      <p class="person-role">Project Manager</p>
    </div>

    <span class="contact-rail"></span>
    <ul class="contact-list">
      <li class="contact-item" style="top:354px">
        <span class="contact-icon">
          <svg width="18" height="18" viewBox="0 0 24 24"><path fill="#fff" d="M6.6 10.8c1.4 2.8 3.8 5.1 6.6 6.6l2.2-2.2c.3-.3.7-.4 1-.2 1.1.4 2.3.6 3.6.6.6 0 1 .4 1 1V20c0 .6-.4 1-1 1C10.6 21 3 13.4 3 4c0-.6.4-1 1-1h3.5c.6 0 1 .4 1 1 0 1.3.2 2.5.6 3.6.1.3 0 .7-.2 1l-2.3 2.2z"/></svg>
        </span>
        (441) 555-0187
      </li>
      <li class="contact-item contact-email" style="top:409px">
        <span class="contact-icon">
          <svg width="18" height="14" viewBox="0 0 24 18"><rect x="1" y="1" width="22" height="16" fill="none" stroke="#fff" stroke-width="2"/><path d="M1 1l11 9 11-9M1 17l8-7M23 17l-8-7" fill="none" stroke="#fff" stroke-width="1.6"/></svg>
        </span>
        twlelectricalsoultions@mailpost-demo.com
      </li>
      <li class="contact-item" style="top:469px">
        <span class="contact-icon" aria-label="Social profile"></span>
        @twlelectricalsolutions
      </li>
      <li class="contact-item" style="top:529px">
        <span class="contact-icon" aria-label="Social profile"></span>
        @twlelectricalsolutions
      </li>
    </ul>
  </section>

  <section class="card card-back" aria-label="Card back">
    <div class="circuit-band" role="img" aria-label="Decorative circuit-trace pattern in soft blue-grey"></div>

    <div class="wordmark back-logo">
      <span class="wordmark-dot"></span>
      <span>Tidewell Electrical Solutions</span>
    </div>

    <ul class="service-list">
      <li class="service" style="top:358px">
        <svg class="service-plug" viewBox="0 0 76 25"><rect x="0" y="11" width="40" height="3" fill="#fff"/><rect x="38" y="7" width="6" height="11" rx="2" fill="#fff"/><rect x="44" y="8.5" width="4" height="2" fill="#fff"/><rect x="44" y="14.5" width="4" height="2" fill="#fff"/></svg>
        <span>Electrical Construction<br>&amp; Maintenance</span>
      </li>
      <li class="service" style="top:432px">
        <svg class="service-plug" viewBox="0 0 76 25"><rect x="0" y="11" width="40" height="3" fill="#fff"/><rect x="38" y="7" width="6" height="11" rx="2" fill="#fff"/><rect x="44" y="8.5" width="4" height="2" fill="#fff"/><rect x="44" y="14.5" width="4" height="2" fill="#fff"/></svg>
        <span>LED Lighting &amp; Automation</span>
      </li>
      <li class="service" style="top:480px">
        <svg class="service-plug" viewBox="0 0 76 25"><rect x="0" y="11" width="40" height="3" fill="#fff"/><rect x="38" y="7" width="6" height="11" rx="2" fill="#fff"/><rect x="44" y="8.5" width="4" height="2" fill="#fff"/><rect x="44" y="14.5" width="4" height="2" fill="#fff"/></svg>
        <span>Life Safety Systems<br>(Fire Alarm / Security)</span>
      </li>
      <li class="service" style="top:555px">
        <svg class="service-plug" viewBox="0 0 76 25"><rect x="0" y="11" width="40" height="3" fill="#fff"/><rect x="38" y="7" width="6" height="11" rx="2" fill="#fff"/><rect x="44" y="8.5" width="4" height="2" fill="#fff"/><rect x="44" y="14.5" width="4" height="2" fill="#fff"/></svg>
        <span>Data &amp; Communication</span>
      </li>
    </ul>
  </section>

</main>
</body>
</html>
```